Silver Brook Decorators Banner

Create a banner that displays and reinforces Silver Brook Decorators’ brand identity while promoting our interior painting services. The banner will be displayed at indoor venues through the winter. The design should be clean, professional, and visually recognizable to both new and returning customers. See attached design brief & logo source files.

```html
<!DOCTYPE html>
<html lang="en">
<head>
<meta charset="utf-8">
<title>Silver Brook Decorators Banner</title>
<link href="https://fonts.googleapis.com/css2?family=Poppins:wght@600;700;800&family=Bebas+Neue&display=swap" rel="stylesheet">
<style>
  :root {
    --stage: #b1b4ae;
    --ink: #464646;
    --dark: #3a3a3a;
    --dark-2: #4b4b4b;
    --green: #6d9257;
    --white: #ffffff;
  }
  * { box-sizing: border-box; margin: 0; padding: 0; }
  html, body { width: 1068px; height: 1200px; overflow: hidden; }
  body { background: var(--stage); font-family: "Poppins", sans-serif; position: relative; }

  .banner {
    position: absolute; left: 34px; top: 400px;
    width: 1000px; height: 399px;
    background: var(--white);
    overflow: hidden;
    box-shadow: 0 16px 40px rgba(0,0,0,0.28);
  }
  .room-photo {
    position: absolute; left: 0; top: 188px; width: 1000px; height: 211px;
    background: linear-gradient(100deg, var(--dark) 0%, var(--dark-2) 55%, var(--dark) 100%);
  }
  .white-cap { position: absolute; left: 0; top: 0; width: 1000px; height: 272px; }

  .headline { position: absolute; left: 38px; top: 24px; line-height: 1; }
  .headline__line { display: block; font-weight: 800; font-size: 75px; letter-spacing: -1px; color: var(--ink); }
  .headline__line--green { color: var(--green); margin-top: -4px; font-size: 76px; }
  .headline__since {
    display: block; font-family: "Bebas Neue", sans-serif; font-size: 74px;
    color: var(--ink); margin-top: 2px; letter-spacing: -1px;
  }

  .brand-name {
    position: absolute; left: 736px; top: 62px; width: 230px;
    font-weight: 800; font-size: 27px; line-height: 1.1; color: var(--ink);
    text-transform: uppercase;
  }

  .services { position: absolute; left: 359px; top: 196px; color: var(--white); }
  .services__title { font-weight: 700; font-size: 21px; letter-spacing: 0.22em; white-space: nowrap; }
  .service {
    position: absolute; display: flex; align-items: flex-start; gap: 12px;
    font-weight: 600; font-size: 22px; line-height: 1.15; white-space: nowrap;
  }
  .service svg { width: 20px; height: 20px; margin-top: 3px; flex: none; }

  .cta {
    position: absolute; left: 38px; top: 318px; width: 914px; height: 54px;
    background: var(--green); border-radius: 27px;
  }
  .cta__label {
    position: absolute; left: 22px; top: 0; line-height: 54px;
    color: var(--white); font-weight: 700; font-size: 26px; letter-spacing: -0.3px;
  }
  .cta__url {
    position: absolute; left: 418px; top: 0; width: 496px; height: 54px;
    background: var(--white); border-radius: 27px;
    display: flex; align-items: center; gap: 14px; padding-left: 18px;
  }
  .cta__url svg { width: 26px; height: 26px; flex: none; }
  .cta__url span { font-weight: 800; font-size: 35px; color: var(--dark); letter-spacing: -0.5px; }
  .cta__url .accent { color: var(--green); font-weight: 800; }
</style>
</head>
<body>
  <section class="banner">
    <div class="room-photo" role="img" aria-label="Softly darkened photo of a freshly painted living room interior"></div>
    <svg class="white-cap" viewBox="0 0 1000 272" aria-hidden="true">
      <path fill="#ffffff" d="M0 0 H1000 V188 H360 C340 188 330 200 330 222 V238 C330 260 318 272 296 272 H0 Z"/>
    </svg>

    <h1 class="headline">
      <span class="headline__line">TRUSTED LOCAL</span>
      <span class="headline__line headline__line--green">PROFESSIONALS</span>
      <span class="headline__since">SINCE 2005</span>
    </h1>

    <div class="brand-name">Silver Brook Decorators</div>

    <div class="services">
      <div class="services__title">INTERIOR PAINTING SERVICES</div>
    </div>

    <svg width="0" height="0" style="position:absolute">
      <symbol id="tick" viewBox="0 0 20 20">
        <circle cx="10" cy="10" r="9.5" fill="#ffffff"/>
        <circle cx="10" cy="10" r="7" fill="#6d9257"/>
        <path d="M6.3 10.2 L8.9 12.7 L13.8 7.6" fill="none" stroke="#ffffff" stroke-width="1.8" stroke-linecap="round" stroke-linejoin="round"/>
      </symbol>
    </svg>

    <div class="service" style="left:370px; top:238px; color:#fff"><svg><use href="#tick"/></svg><span style="margin-left:12px">Walls</span></div>
    <div class="service" style="left:370px; top:276px; color:#fff"><svg><use href="#tick"/></svg><span style="margin-left:12px">Ceilings</span></div>
    <div class="service" style="left:587px; top:238px; color:#fff"><svg><use href="#tick"/></svg><span style="margin-left:2px">Trim</span></div>
    <div class="service" style="left:587px; top:276px; color:#fff"><svg><use href="#tick"/></svg><span style="margin-left:2px">Cabinets</span></div>
    <div class="service" style="left:803px; top:238px; color:#fff"><svg><use href="#tick"/></svg><span style="margin-left:5px">Drywall<br>Repair</span></div>

    <div class="cta">
      <div class="cta__label">Book a Free Estimate at</div>
      <div class="cta__url">
        <svg viewBox="0 0 26 26" aria-hidden="true">
          <g fill="none" stroke="#3a3a3a" stroke-width="2">
            <circle cx="13" cy="13" r="11"/>
            <ellipse cx="13" cy="13" rx="4.5" ry="11"/>
            <path d="M2 13 H24 M4 7.5 H22 M4 18.5 H22"/>
          </g>
        </svg>
        <span>www.<span class="accent">sbdecorators</span>.com</span>
      </div>
    </div>
  </section>
</body>
</html>
```